Harbor Fieldworks (Business Card Design)

Need business cards designed. Something modern, chic, and sleek. Mabye the back of the card should be the navy blue that is in the logo and then just the logo on the back.

Target Market(s)

Those in the hotel, office, and renovation industry

Contact Information for Business Card

1. Logo 2. Dorian Velasko 3. CEO/Founder 4. Phone: (833) HarbFld / (833) 427-2353 5. Email: dorian@theharborfieldworks.com 6. Website: www.theharborfieldworks.com

Font styles to use
Other font styles liked:
• Look at the logo font and base the font for everything else off of that.

Colors
0054AA
0677BA
7BADD7
CADEEF
E8F1F8

Requirements
Must have
• Colors that are associated in the logo
Nice to have
• Sleek modern clean and chic design.

```html
<!DOCTYPE html>
<html lang="en">
<head>
<meta charset="utf-8">
<title>Harbor Fieldworks – Business Card</title>
<link href="https://fonts.googleapis.com/css2?family=Montserrat:wght@600;700&family=Open+Sans:wght@400;600&display=swap" rel="stylesheet">
<style>
  :root {
    --backdrop: #1d1d21;
    --navy: #0d1846;
    --navy-light: #1a2656;
    --gold: #d2a64a;
    --white: #ffffff;
    --ink-soft: #dfe3ef;
  }
  * { box-sizing: border-box; margin: 0; padding: 0; }
  html, body {
    width: 1200px; height: 780px; overflow: hidden;
    background: var(--backdrop);
  }
  .canvas { position: relative; width: 1200px; height: 780px; }

  .card {
    position: absolute;
    width: 540px; height: 310px;
    background: var(--navy);
    border-radius: 22px;
    border-bottom: 3px solid var(--gold);
    border-right: 3px solid var(--gold);
    overflow: hidden;
    box-shadow: 0 18px 40px rgba(0,0,0,.55);
  }
  .card--back  { left: 60px;  top: 70px; }
  .card--front { left: 600px; top: 400px; }

  /* back side */
  .back-wordmark {
    position: absolute; inset: 0;
    display: flex; align-items: center; justify-content: center; gap: 12px;
    font-family: "Montserrat", sans-serif; font-weight: 700;
    font-size: 30px; letter-spacing: 4px; text-transform: uppercase;
    color: var(--navy-light);
  }
  .back-wordmark .mark-square { width: 18px; height: 18px; background: var(--navy-light); }

  /* front side */
  .name-tab {
    position: absolute; top: 30px; right: 0;
    width: 14px; height: 30px; background: var(--gold);
  }
  .identity {
    position: absolute; top: 26px; right: 26px; text-align: right;
  }
  .person-name {
    font-family: "Montserrat", sans-serif; font-weight: 700; font-size: 26px;
    line-height: 1.1;
  }
  .person-name .first { color: var(--gold); }
  .person-name .last  { color: var(--white); }
  .person-title {
    font-family: "Open Sans", sans-serif; font-size: 13px; color: var(--white);
    margin-top: 3px;
  }

  .company {
    position: absolute; left: 30px; top: 118px;
    display: flex; align-items: center; gap: 8px;
    font-family: "Montserrat", sans-serif; font-weight: 700;
    font-size: 17px; letter-spacing: 2px; text-transform: uppercase;
    color: var(--white);
  }
  .company .mark-square { width: 10px; height: 10px; background: var(--gold); }

  .address {
    position: absolute; left: 30px; top: 152px;
    font-family: "Open Sans", sans-serif; font-size: 12.5px; line-height: 1.5;
    color: var(--ink-soft);
  }
  .contacts {
    position: absolute; left: 30px; bottom: 24px;
    list-style: none;
    font-family: "Open Sans", sans-serif; font-size: 12.5px; line-height: 1.65;
    color: var(--white);
  }
  .contacts li { display: flex; align-items: center; gap: 8px; }
  .contacts svg { width: 12px; height: 12px; flex: none; }
</style>
</head>
<body>
<main class="canvas">

  <section class="card card--back" aria-label="Card back">
    <div class="back-wordmark"><span class="mark-square"></span>Harbor Fieldworks</div>
  </section>

  <section class="card card--front" aria-label="Card front">
    <span class="name-tab"></span>
    <div class="identity">
      <p class="person-name"><span class="first">Dorian</span> <span class="last">Velasko</span></p>
      <p class="person-title">CEO/Founder</p>
    </div>

    <div class="company"><span class="mark-square"></span>Harbor Fieldworks</div>

    <p class="address">4127 Marlow Park Rd<br>Suite 210, Eastbrook, MD 21960</p>

    <ul class="contacts">
      <li>
        <svg viewBox="0 0 24 24" aria-hidden="true"><path fill="#d2a64a" d="M6.6 10.8a15 15 0 0 0 6.6 6.6l2.2-2.2a1 1 0 0 1 1-.25 11.4 11.4 0 0 0 3.6.6 1 1 0 0 1 1 1V20a1 1 0 0 1-1 1A17 17 0 0 1 3 4a1 1 0 0 1 1-1h3.5a1 1 0 0 1 1 1c0 1.25.2 2.45.6 3.6a1 1 0 0 1-.25 1z"/></svg>
        (833) HarbFld / (833) 427-2353
      </li>
      <li>
        <svg viewBox="0 0 24 24" aria-hidden="true"><circle cx="12" cy="12" r="9" fill="none" stroke="#d2a64a" stroke-width="2"/><path d="M3 12h18M12 3c3 3 3 15 0 18M12 3c-3 3-3 15 0 18" fill="none" stroke="#d2a64a" stroke-width="1.6"/></svg>
        www.theharborfieldworks.com
      </li>
      <li>
        <svg viewBox="0 0 24 24" aria-hidden="true"><rect x="3" y="5" width="18" height="14" rx="1.5" fill="none" stroke="#d2a64a" stroke-width="2"/><path d="M3.5 6l8.5 7 8.5-7" fill="none" stroke="#d2a64a" stroke-width="2"/></svg>
        dorian@theharborfieldworks.com
      </li>
    </ul>
  </section>

</main>
</body>
</html>
```